Velmont Chamber of Commerce Website

We have been asked to design a new website for the Velmont Chamber of Commerce. The mission of the Greater Velmont Chamber of Commerce is to develop and promote an economically vibrant business community aggressively. The website should reflect a modern, professional design that showcases local businesses and promotes the programs the Chamber has to offer.

```html
<!DOCTYPE html>
<html lang="en">
<head>
<meta charset="utf-8">
<title>Greater Velmont Chamber of Commerce</title>
<link href="https://fonts.googleapis.com/css2?family=Roboto:wght@400;500;700&display=swap" rel="stylesheet">
<style>
:root{
  --navy:#1d3b6f;
  --blue:#3a67b1;
  --grey-bg:#f4f4f4;
  --text:#6a6a6a;
  --dark:#333a45;
  --white:#ffffff;
}
*{box-sizing:border-box;margin:0;padding:0}
html,body{width:1200px;height:3812px;overflow:hidden}
body{font-family:'Roboto',sans-serif;color:var(--text);background:var(--white);position:relative}
.abs{position:absolute}
a{color:inherit;text-decoration:none}

/* header */
.brand{left:111px;top:18px;height:68px;display:flex;align-items:center;gap:12px}
.brand-dot{width:64px;height:64px;border-radius:50%;background:var(--navy)}
.brand-name{color:var(--navy);font-weight:700;font-size:19px;line-height:22px;text-transform:uppercase}
.toplinks{right:111px;top:33px;font-size:12px;font-weight:500;color:#666;display:flex;gap:12px;align-items:center}
.toplinks .sep{color:#aaa}

/* hero */
.hero{left:0;top:100px;width:1200px;height:600px;background:linear-gradient(120deg,#8e98a3 0%,#c9ced3 45%,#9aa3ab 75%,#6e757c 100%)}
.hero-panel{left:0;top:100px}
.hero-title{left:111px;top:276px;color:#fff;font-size:37px;font-weight:500;line-height:47px;letter-spacing:.5px}
.hero-sub{left:111px;top:386px;width:540px;color:#fff;font-size:16.5px;line-height:27px}
.btn-white{left:111px;top:465px;width:145px;height:49px;background:#fff;color:var(--navy);font-size:14px;font-weight:500;text-align:center;line-height:49px}
.dots{left:563px;top:662px;display:flex;gap:8px}
.dots i{width:12px;height:12px;border-radius:50%;border:1.5px solid #fff;display:block}
.dots i.on{background:#fff}

/* main navigation, drawn above the hero */
.navbar{left:474px;top:80px;width:726px;height:40px;background:var(--navy);z-index:5}
.navbar-slant{left:440px;top:80px;z-index:5}
.navbar ul{list-style:none;display:flex;gap:20px;position:absolute;left:22px;top:0;height:40px;align-items:center;color:#fff;font-size:11.5px;font-weight:700;white-space:nowrap}
.navbar li{display:flex;align-items:center;gap:5px}

/* about */
.h2{font-size:36px;font-weight:700;color:var(--navy);letter-spacing:.5px}
.h2 em{font-style:normal;color:var(--blue)}
.about-text{left:640px;top:950px;width:449px;font-size:14.5px;line-height:25.6px;text-align:justify}
.btn-blue{left:640px;top:1141px;width:145px;height:49px;background:var(--blue);color:#fff;font-size:14px;font-weight:500;text-align:center;line-height:49px}

/* programs */
.programs{left:0;top:1379px;width:1200px;height:591px;background:var(--grey-bg)}
.card{top:1545px;width:235px;height:333px;color:#fff;text-align:center;padding:0 12px}
.card.dark{background:var(--navy)}
.card.mid{background:var(--blue)}
.card svg{display:block;margin:26px auto 0}
.card h3{font-size:16px;font-weight:500;line-height:26px;margin-top:16px;text-transform:uppercase}
.card p{font-size:13px;line-height:23px;margin-top:8px;height:115px;overflow:hidden}
.card .more{font-size:12px;font-weight:700;margin-top:10px;display:block}
.arrow-btn{width:36px;height:36px;border-radius:50%;background:#fff;box-shadow:0 2px 6px rgba(0,0,0,.15);display:flex;align-items:center;justify-content:center}

/* testimonial */
.quote-text{left:402px;top:2200px;width:675px;font-size:15.5px;line-height:26.6px;text-align:justify}
.quote-text a{color:var(--blue);font-weight:500}
.quote-name{left:402px;top:2321px;font-size:13.5px;color:var(--navy)}
.quote-name b{font-size:16px}

/* partners */
.partners{left:0;top:2436px;width:1200px;height:327px;background:linear-gradient(180deg,#3a67b1,#2f5aa3 60%,#3a67b1)}
.partner{top:2597px;width:176px;height:86px;background:#fff;border-radius:4px;display:flex;align-items:center;justify-content:center}
.partner i{width:48px;height:48px;border-radius:50%;background:#d6deeb;display:block}

/* news */
.news-img{top:2951px;width:308px;height:206px}
.news-img.one{background:linear-gradient(160deg,#5b7f97,#2f4555 60%,#1c2a33)}
.news-img.two{background:linear-gradient(160deg,#e2e4e6,#9aa0a6 55%,#3c4146)}
.news-img.three{background:linear-gradient(160deg,#6b4a30,#3b2a1e 55%,#a9876a)}
.news-body{top:3176px;width:308px;padding:0 14px 0 16px}
.news-body h4{font-size:16.5px;font-weight:500;line-height:25px;color:var(--dark);text-transform:uppercase;white-space:nowrap}
.meta{font-size:13px;color:#a0a0a0;margin-top:6px;display:flex;gap:18px}
.news-body p{font-size:13px;line-height:23px;margin-top:8px;height:69px;overflow:hidden}
.news-body .more{display:block;font-size:13px;font-weight:700;color:var(--blue);margin-top:6px}
.news-rule{top:3176px;width:2px;height:180px;background:linear-gradient(180deg,var(--navy) 0 50px,#e2e2e2 50px)}

/* footer */
.footer{left:0;top:3442px;width:1200px;height:370px;background:var(--navy);color:#fff}
.foot-brand{left:0;width:1200px;top:3492px;display:flex;justify-content:center;align-items:center;gap:12px}
.foot-brand .brand-dot{background:#fff;width:60px;height:60px}
.foot-brand .brand-name{color:#fff}
.foot-nav{left:0;width:1200px;text-align:center;font-size:14.5px;font-weight:500;color:#fff}
.foot-nav .sep{margin:0 12px}
.foot-contact{left:0;width:1200px;top:3655px;text-align:center;font-size:13.5px;color:#fff}
.socials{left:511px;top:3690px;display:flex;gap:4px}
.socials i{width:32px;height:32px;border-radius:50%;background:#fff;display:block}
.socials i.first{background:var(--blue)}
.foot-line{left:111px;top:3752px;width:978px;height:1px;background:rgba(255,255,255,.25)}
.copy{left:0;width:1200px;top:3771px;text-align:center;font-size:13px;color:#fff}
</style>
</head>
<body>

<!-- header -->
<div class="abs brand">
  <span class="brand-dot"></span>
  <span class="brand-name">Greater Velmont<br>Chamber of Commerce</span>
</div>
<nav class="abs toplinks"><span>ECONOMIC</span><span class="sep">|</span><span>JOIN OUR EMAIL LIST</span><span class="sep">|</span><span>COMMUNITY</span><span class="sep">|</span><span>RESOURCES</span><span class="sep">|</span>
<svg width="13" height="13" viewBox="0 0 13 13"><circle cx="5.5" cy="5.5" r="4" fill="none" stroke="#666" stroke-width="1.8"/><line x1="8.5" y1="8.5" x2="12" y2="12" stroke="#666" stroke-width="1.8"/></svg></nav>

<!-- hero -->
<div class="abs hero" role="img" aria-label="Photo of two colleagues walking through a bright open-plan office"></div>
<svg class="abs hero-panel" width="710" height="600"><polygon points="0,141 707,141 420,600 0,600" fill="#3a67b1" opacity=".55"/></svg>
<h1 class="abs hero-title">GREATER VELMONT<br>CHAMBER OF COMMERCE</h1>
<p class="abs hero-sub">Greater Velmont Chamber of Commerce is to aggressively develop and promote an economically vibrant business community.</p>
<a class="abs btn-white">LEARN MORE</a>
<div class="abs dots"><i></i><i class="on"></i><i></i><i></i></div>

<!-- main navigation -->
<svg class="abs navbar-slant" width="35" height="40"><polygon points="26,0 35,0 35,40 0,40" fill="#1d3b6f"/></svg>
<nav class="abs navbar">
  <ul>
    <li>HOME</li>
    <li>BUSINESS RESOURCES<svg width="8" height="5"><polyline points="1,1 4,4 7,1" fill="none" stroke="#fff" stroke-width="1.3"/></svg></li>
    <li>PROGRAMS<svg width="8" height="5"><polyline points="1,1 4,4 7,1" fill="none" stroke="#fff" stroke-width="1.3"/></svg></li>
    <li>MEMBERSHIP<svg width="8" height="5"><polyline points="1,1 4,4 7,1" fill="none" stroke="#fff" stroke-width="1.3"/></svg></li>
    <li>EVENTS<svg width="8" height="5"><polyline points="1,1 4,4 7,1" fill="none" stroke="#fff" stroke-width="1.3"/></svg></li>
    <li>CONTACT US<svg width="8" height="5"><polyline points="1,1 4,4 7,1" fill="none" stroke="#fff" stroke-width="1.3"/></svg></li>
  </ul>
</nav>

<!-- about -->
<svg class="abs" style="left:105px;top:799px" width="490" height="490">
  <circle cx="241" cy="241" r="237" fill="#fff" stroke="#1d3b6f" stroke-width="5"/>
</svg>
<div class="abs" role="img" aria-label="Photo of two business people reviewing notes at a laptop" style="left:124px;top:818px;width:444px;height:444px;border-radius:50%;background:radial-gradient(circle at 50% 40%,#d7d2c9,#9a8d80 70%,#5a5148)"></div>
<div class="abs" style="left:424px;top:1116px;width:156px;height:156px;border-radius:50%;background:#fff;box-shadow:0 4px 14px rgba(0,0,0,.2)"></div>
<div class="abs" style="left:436px;top:1128px;width:132px;height:132px;border-radius:50%;border:4px solid var(--navy)"></div>
<div class="abs" style="left:468px;top:1160px;width:68px;height:68px;border-radius:50%;background:var(--navy)"></div>
<h2 class="abs h2" style="left:640px;top:880px">ABOUT <em>US</em></h2>
<p class="abs about-text">The Chamber, in both its values and practices, is committed to inclusion and excellence in the management of all diverse people irrespective of differences. This means that there shall be no barriers to participation in any activity of the Chamber on the basis of economic position, gender, race, creed, age, sexual orientation, gender identity, national origin, or disability.</p>
<a class="abs btn-blue">LEARN MORE</a>

<!-- programs -->
<section class="abs programs"></section>
<h2 class="abs h2" style="left:0;width:1200px;text-align:center;top:1462px">OUR <em>PROGRAMS</em></h2>

<div class="abs card dark" style="left:111px">
  <svg width="54" height="54" viewBox="0 0 54 54" fill="none" stroke="#fff" stroke-width="2"><circle cx="27" cy="22" r="14"/><circle cx="27" cy="22" r="6"/><path d="M8 40l10-6 9 5 9-5 10 6"/><path d="M8 40l6 8h26l6-8"/></svg>
  <h3>Business<br>Education Alliance</h3>
  <p>In the early 1990's the Greater Velmont Chamber of Commerce started several education-related programs to introduce or prepare students for the workforce.</p>
  <span class="more">LEARN MORE &#10148;</span>
</div>
<div class="abs card mid" style="left:358px">
  <svg width="54" height="54" viewBox="0 0 54 54" fill="none" stroke="#fff" stroke-width="2"><rect x="14" y="6" width="28" height="40" rx="2"/><line x1="20" y1="16" x2="36" y2="16"/><line x1="20" y1="23" x2="36" y2="23"/><line x1="24" y1="30" x2="36" y2="30"/><circle cx="14" cy="32" r="5"/><path d="M11 37l-2 9 5-3 5 3-2-9"/></svg>
  <h3>Certificates of<br>Origin</h3>
  <p>The Greater Velmont Chamber of Commerce offers Certificates of Origin for both Members and Non-members.</p>
  <span class="more">LEARN MORE &#10148;</span>
</div>
<div class="abs card dark" style="left:605px">
  <svg width="54" height="54" viewBox="0 0 54 54" fill="none" stroke="#fff" stroke-width="2"><rect x="10" y="6" width="24" height="30"/><line x1="15" y1="14" x2="29" y2="14"/><line x1="15" y1="20" x2="29" y2="20"/><path d="M22 48V38l12-7 12 7v10z"/><line x1="27" y1="40" x2="27" y2="48"/><line x1="34" y1="40" x2="34" y2="48"/><line x1="41" y1="40" x2="41" y2="48"/></svg>
  <h3>Government<br>Relations Council</h3>
  <p>Join the Greater Velmont Chamber of Commerce as we work to improve the future of our economic community. Help us increase our influence with various legislative</p>
  <span class="more">LEARN MORE &#10148;</span>
</div>
<div class="abs card mid" style="left:852px">
  <svg width="54" height="54" viewBox="0 0 54 54" fill="none" stroke="#fff" stroke-width="2"><circle cx="27" cy="27" r="20"/><circle cx="27" cy="27" r="13"/><path d="M27 3v5M27 46v5M3 27h5M46 27h5M10 10l4 4M40 40l4 4M44 10l-4 4M10 44l4-4"/><path d="M22 32v-8l5-4 5 4v8"/></svg>
  <h3>Leadership<br>Velmont</h3>
  <p>Founded in 1981, Leadership Velmont is California's oldest adult community leadership program. Leadership Velmont is a program designed to inspire a new</p>
  <span class="more">LEARN MORE &#10148;</span>
</div>
<div class="abs arrow-btn" style="left:37px;top:1694px"><svg width="10" height="14"><polyline points="8,1 2,7 8,13" fill="none" stroke="#1d3b6f" stroke-width="2"/></svg></div>
<div class="abs arrow-btn" style="left:1126px;top:1694px"><svg width="10" height="14"><polyline points="2,1 8,7 2,13" fill="none" stroke="#1d3b6f" stroke-width="2"/></svg></div>

<!-- testimonial -->
<h2 class="abs h2" style="left:0;width:1200px;text-align:center;top:2063px;font-size:32px">WHY OUR <em>MEMBERS LOVE US!</em></h2>
<div class="abs" role="img" aria-label="Portrait photo of a smiling member in a denim shirt" style="left:122px;top:2144px;width:196px;height:196px;border-radius:50%;background:radial-gradient(circle at 50% 45%,#c9b8a4,#8e8a86 65%,#5f6770)"></div>
<div class="abs" style="left:360px;top:2175px;width:1px;height:133px;background:#d8d8d8"></div>
<svg class="abs" style="left:402px;top:2144px" width="46" height="38" viewBox="0 0 46 38"><path d="M0 38V20C0 8 6 1 18 0v7c-6 1-9 5-9 11h9v20zM26 38V20C26 8 32 1 44 0v7c-6 1-9 5-9 11h9v20z" fill="#3a67b1"/></svg>
<p class="abs quote-text">I wanted to comment on the outstanding service and support that the Velmont Chamber of Commerce has provided during these trying times.&nbsp; As I had mentioned to you, when times are good and smooth, I think we take for granted the excellent work (year-round) that The Chamber conducts in support of our local business and community... <a>Read More!</a></p>
<p class="abs quote-name"><b>GRAHAM T. ELLISON,</b> Ellison Heating &amp; Air Conditioning, Inc.</p>

<!-- partners -->
<section class="abs partners"></section>
<h2 class="abs h2" style="left:0;width:1200px;text-align:center;top:2508px;color:#fff">OUR PARTNERS</h2>
<div class="abs partner" style="left:111px"><i></i></div>
<div class="abs partner" style="left:312px"><i></i></div>
<div class="abs partner" style="left:512px"><i></i></div>
<div class="abs partner" style="left:713px"><i></i></div>
<div class="abs partner" style="left:912px"><i></i></div>
<svg class="abs" style="left:50px;top:2627px" width="20" height="28"><polyline points="16,2 4,14 16,26" fill="none" stroke="#fff" stroke-width="3"/></svg>
<svg class="abs" style="left:1128px;top:2627px" width="20" height="28"><polyline points="4,2 16,14 4,26" fill="none" stroke="#fff" stroke-width="3"/></svg>

<!-- news -->
<h2 class="abs h2" style="left:0;width:1200px;text-align:center;top:2864px">LATEST <em>NEWS</em></h2>

<div class="abs news-img one" style="left:111px" role="img" aria-label="Photo of a business meeting in a glass-walled conference room"></div>
<div class="abs news-img two" style="left:445px" role="img" aria-label="Photo of two colleagues discussing work at a computer"></div>
<div class="abs news-img three" style="left:780px" role="img" aria-label="Photo of a woman reading from a tablet in a warm-lit room"></div>

<div class="abs news-body" style="left:111px"><h4>Thank you to our new &amp;<br>renewing members</h4><div class="meta"><span>&#128100; DANA WHITFIELD</span><span>&#128197; 16 DEC 2022</span></div><p>Thank you to our new &amp; renewing Members for your continued support of the Greater Velmont Chamber of Commerce.</p><span class="more">READ MORE &#10148;</span></div>
<div class="abs news-rule" style="left:418px"></div>
<div class="abs news-body" style="left:445px"><h4>January 5th networking mixer<br>at the Orchard Lane Theatre</h4><div class="meta"><span>&#128100; DANA WHITFIELD</span><span>&#128197; 15 DEC 2022</span></div><p>Mark your calendar for the Velmont Chamber of Commerce January Networking Mixer at the Orchard Lane Theatre! Join us:</p><span class="more">READ MORE &#10148;</span></div>
<div class="abs news-rule" style="left:752px"></div>
<div class="abs news-body" style="left:780px"><h4>Webinar 1/17/22 – 2023<br>Labor Law Update</h4><div class="meta"><span>&#128100; DANA WHITFIELD</span><span>&#128197; 15 DEC 2022</span></div><p>2023 Labor Law Update Tuesday, January 17, 2023 10:00am – 11:00am PST Register Here 2021 AND 2022 were unprecedented years!</p><span class="more">READ MORE &#10148;</span></div>
<div class="abs news-rule" style="left:1087px"></div>

<!-- footer -->
<footer class="abs footer"></footer>
<div class="abs foot-brand"><span class="brand-dot"></span><span class="brand-name">Greater Velmont<br>Chamber of Commerce</span></div>
<div class="abs foot-nav" style="top:3580px">HOME<span class="sep">|</span>BUSINESS RESOURCES<span class="sep">|</span>PROGRAMS<span class="sep">|</span>MEMBERSHIP<span class="sep">|</span>EVENTS<span class="sep">|</span>CONTACT US</div>
<div class="abs foot-nav" style="top:3616px">ECONOMIC<span class="sep">|</span>JOIN OUR EMAIL LIST<span class="sep">|</span>COMMUNITY<span class="sep">|</span>RESOURCES</div>
<div class="abs foot-contact">
  <svg width="12" height="12" viewBox="0 0 12 12"><path d="M2 1l2 0 1 3-1.5 1a7 7 0 0 0 3.5 3.5L8 7l3 1v2c0 1-1 1-1 1A9 9 0 0 1 1 2s0-1 1-1z" fill="#fff"/></svg>
  &nbsp;+1 555-014-2270 &nbsp;&nbsp;|&nbsp;&nbsp;
  <svg width="14" height="11" viewBox="0 0 14 11"><rect x="0.5" y="0.5" width="13" height="10" fill="#fff"/><polyline points="0.5,0.5 7,6 13.5,0.5" fill="none" stroke="#1d3b6f" stroke-width="1.2"/></svg>
  &nbsp;hello@velmontchamber.org
</div>
<div class="abs socials"><i class="first"></i><i></i><i></i><i></i><i></i></div>
<div class="abs foot-line"></div>
<p class="abs copy">© 2022 Greater Velmont Chamber of Commerce &nbsp;&nbsp;|&nbsp;&nbsp; All Rights Reserved</p>

</body>
</html>
```